" Somos uma fábrica de Creme de Café, um produto inovador tanto no sabor quanto no modo de preparo. O Café Velurê é um creme de café 100% arábica, saborizado naturalmente que faz uma bebida extremamente cremosa e diferenciada. Até quem não gosta de café, quando prova o Café Velurê passa a gostar. Nossos produtos são 100% naturais e nosso café é de altíssima qualidade, pois utilizamos café 100% arábica. Buscamos constante inovação na formulação de nossos produtos. Temos uma linguagem de comunicação informal, leve e descontraída com nossos clientes, sem ser infantil, . "

```html
<!DOCTYPE html>
<html lang="pt-BR">
<head>
<meta charset="utf-8">
<title>Café Velurê – Rótulo Baunilha</title>
<link rel="stylesheet" href="https://fonts.googleapis.com/css2?family=Fredoka:wght@400;500;600;700&family=Lilita+One&family=Patrick+Hand&display=swap">
<style>
  :root {
    --canvas: #e6e0de;
    --label-paper: #f1ecea;
    --label-band: #d3cacc;
    --band-shade: #c7bdc0;
    --brown: #5b3b30;
    --brown-soft: #7a5a4f;
  }
  * { margin: 0; padding: 0; box-sizing: border-box; }
  html, body { width: 1200px; height: 1200px; overflow: hidden; }
  body { background: var(--canvas); position: relative; font-family: "Fredoka", sans-serif; color: var(--brown); }

  .label {
    position: absolute; left: 50px; top: 330px; width: 1100px; height: 540px;
    background: var(--label-paper);
    box-shadow: 0 6px 24px rgba(60, 40, 35, 0.12);
    overflow: hidden;
  }
  .bean-band {
    position: absolute; left: 0; top: 300px; width: 800px; height: 240px;
    background: linear-gradient(180deg, var(--label-band), var(--band-shade));
  }
  .front { position: absolute; left: 0; top: 0; width: 800px; height: 540px; }
  .side {
    position: absolute; left: 800px; top: 0; width: 300px; height: 540px;
    border-left: 2px solid var(--label-band);
    padding: 34px 28px; font-size: 15px; line-height: 1.35;
  }
  .side h3 { font-weight: 600; font-size: 19px; margin-bottom: 6px; }
  .side p { margin-bottom: 22px; }
  .nutrition { width: 100%; border-collapse: collapse; font-size: 15px; }
  .nutrition td { border-top: 1.5px solid var(--brown-soft); padding: 6px 0; }
  .nutrition td:last-child { text-align: right; }

  .claim {
    position: absolute; left: 0; width: 800px; top: 40px; text-align: center;
    font-weight: 700; font-style: italic; font-size: 32px;
  }
  .brand-name {
    position: absolute; left: 0; width: 800px; top: 110px; text-align: center;
    font-weight: 600; font-size: 66px; line-height: 1;
    white-space: nowrap;
  }
  .product-type {
    position: absolute; left: 0; width: 800px; top: 200px; text-align: center;
    font-weight: 500; font-size: 34px;
  }
  .flavor-intro {
    position: absolute; left: 0; width: 800px; top: 340px; text-align: center;
    font-weight: 500; font-size: 26px;
  }
  .flavor {
    position: absolute; left: 0; width: 800px; top: 376px; text-align: center;
    font-family: "Lilita One", sans-serif; font-size: 66px;
  }
  .volume {
    position: absolute; left: 0; width: 800px; top: 468px; text-align: center;
    font-family: "Patrick Hand", sans-serif; font-size: 22px; line-height: 0.95;
  }

  .badge {
    position: absolute; width: 150px; text-align: center;
    font-family: "Patrick Hand", sans-serif; font-size: 18px; line-height: 1.05; text-transform: uppercase;
  }
  .badge svg { display: block; margin: 0 auto 8px; }
  .badge-additives { left: 20px; top: 48px; }
  .badge-recycle { left: 20px; top: 175px; }
  .badge-gluten { left: 630px; top: 48px; }
  .badge-lactose { left: 630px; top: 175px; }
</style>
</head>
<body>
  <section class="label">
    <div class="bean-band" role="img" aria-label="Faixa com padrão decorativo de grãos de café em tons de lilás acinzentado"></div>

    <div class="front">
      <div class="badge badge-additives">
        <svg width="52" height="52" viewBox="0 0 52 52" fill="none" stroke="var(--brown)" stroke-width="3">
          <circle cx="26" cy="26" r="22"/>
          <path d="M20 16h12M22 16v8l-6 12h20l-6-12v-8"/>
          <line x1="10" y1="42" x2="42" y2="10"/>
        </svg>
        Sem aditivos<br>artificiais
      </div>
      <div class="badge badge-recycle">
        <svg width="52" height="52" viewBox="0 0 52 52" fill="none" stroke="var(--brown)" stroke-width="3">
          <circle cx="26" cy="26" r="22"/>
          <path d="M18 22l5-8 5 8M34 24l4 8h-10M22 34h-8l4-8"/>
        </svg>
        Embalagem<br>100% reciclável
      </div>
      <div class="badge badge-gluten">
        <svg width="52" height="52" viewBox="0 0 52 52" fill="none" stroke="var(--brown)" stroke-width="3">
          <circle cx="26" cy="26" r="22"/>
          <path d="M26 40V14M26 20l-5-4M26 20l5-4M26 27l-5-4M26 27l5-4M26 34l-5-4M26 34l5-4"/>
          <line x1="10" y1="42" x2="42" y2="10"/>
        </svg>
        Sem<br>glúten
      </div>
      <div class="badge badge-lactose">
        <svg width="52" height="52" viewBox="0 0 52 52" fill="none" stroke="var(--brown)" stroke-width="3">
          <circle cx="26" cy="26" r="22"/>
          <path d="M22 12h8v5l3 5v16H19V22l3-5z"/>
          <line x1="10" y1="42" x2="42" y2="10"/>
        </svg>
        Sem<br>lactose
      </div>

      <p class="claim">100% arábica</p>
      <h1 class="brand-name">Café Velurê</h1>
      <p class="product-type">creme de café</p>
      <p class="flavor-intro">sabor natural de</p>
      <p class="flavor">Baunilha</p>
      <p class="volume">contém<br>360ml</p>
    </div>

    <aside class="side">
      <h3>Modo de preparo</h3>
      <p>Misture duas colheres em água quente e mexa bem.</p>
      <h3>Ingredientes</h3>
      <p>Café arábica, açúcar e baunilha natural.</p>
      <h3>Informação nutricional</h3>
      <table class="nutrition">
        <tr><td>Porção</td><td>20 g</td></tr>
        <tr><td>Calorias</td><td>80 kcal</td></tr>
      </table>
    </aside>
  </section>
</body>
</html>
```